Brightway Merch Webpage

Brightway Merc need a simple, elegant and professional website

As the company is selling products and clothes for companies we would like to have a large picture carousel on the top.
As one of the logos have black background I would like the webpage to be black.

There should also be thre boxes on main page where we can have information about the product of the month, news and other.

On the menu we need:
- Our products
-our catalogues (here we need to have the possibility to upload several pdf and e-catalogues
-About us
-Contact us
-News

Here are som pages in the same branch
http://www.kavlemerke.no/
http://www.tavbrud.no/
http://www.merkelund.no/

I will attach the logo with both white and black background.
The logos are attached in png but I have eps and jpg as well. Just let me know what you need.

looking forward to your designs:)

Brightway Merch is a company that provides corporate profile products such as logo on t-shirts, work uniform, pens, cups etc. We also work with event companies that need advertising and profile products for theirs event as well as the sports segment.

Target Market(s)

corporate, eventcompanies and sportsegment

Industry/Entity Type

Advertising

Requirements
Must have
• Facebook, twitter and like button for social media

```html
<!DOCTYPE html>
<html lang="en">
<head>
<meta charset="utf-8">
<title>Brightway Merc</title>
<link href="https://fonts.googleapis.com/css2?family=Ubuntu:wght@300;400;500&family=Kaushan+Script&family=Satisfy&family=Libre+Baskerville&display=swap" rel="stylesheet">
<style>
:root{
  --black:#000;
  --blue:#1b82cb;
  --blue-light:#3aa0e6;
  --blue-dark:#0b5a9c;
  --panel:#2c2c2c;
  --frame:#333;
  --grey-text:#d8d8d8;
  --white:#fff;
}
*{margin:0;padding:0;box-sizing:border-box}
html,body{width:1108px;height:1200px;overflow:hidden;background:var(--black)}
body{position:relative;font-family:Arial,Helvetica,sans-serif;color:var(--white)}
.abs{position:absolute}

.topbar{left:0;top:0;width:1108px;height:48px;background:linear-gradient(#2b93dc,#0f63aa);border-bottom:1px solid #46a6e8}
.logo-tab{left:102px;top:3px;width:214px;height:150px;background:var(--black);border-radius:10px 10px 0 0;text-align:center}
.logo-dot{display:block;width:66px;height:66px;border-radius:50%;background:var(--white);margin:10px auto 12px}
.logo-name{font-family:'Ubuntu',sans-serif;font-weight:400;font-size:25px;color:var(--blue);white-space:nowrap}

.nav{left:0;top:0;width:1108px;height:48px;font-family:'Ubuntu',sans-serif;font-weight:300;font-size:17px;letter-spacing:.5px}
.nav a{position:absolute;top:12px;color:#e6f2fb;text-decoration:none;white-space:nowrap;transform:translateX(-50%)}
.nav .active{top:6px;height:37px;width:122px;padding-top:6px;text-align:center;border-radius:10px;background:linear-gradient(#0e5c9c,#0a4d86);border:1px solid #2e85c5;transform:none;left:483px}

.follow{right:244px;top:68px;font-family:'Satisfy',cursive;font-size:20px;line-height:28px;color:#ddd;white-space:nowrap}
.social{top:68px;width:28px;height:28px;border-radius:50%;background:var(--blue)}
.order{right:104px;top:117px;font-family:'Ubuntu',sans-serif;font-size:20px;white-space:nowrap}
.order b{color:var(--blue);font-weight:500}

.slider{left:106px;top:157px;width:890px;height:418px;background:var(--frame)}
.slide-photo{left:11px;top:10px;width:868px;height:331px;background:linear-gradient(100deg,#5a4a48 0%,#b89a85 30%,#d9c9ad 55%,#cdbb9c 100%)}
.arrow{top:155px;width:84px;height:84px;border-radius:50%;background:var(--white)}
.arrow.prev{left:-42px;clip-path:inset(0 0 0 42px)}
.arrow.next{right:-42px;clip-path:inset(0 42px 0 0)}
.arrow svg{position:absolute;top:27px}
.caption{left:11px;top:341px;width:868px;height:66px;background:var(--black);overflow:hidden}
.caption h3{position:absolute;left:28px;top:7px;font-family:'Libre Baskerville',serif;font-weight:400;font-size:13px;color:var(--blue-light);letter-spacing:-.3px}
.caption p{position:absolute;left:28px;top:29px;width:360px;font-size:11.5px;line-height:17px;color:var(--white)}
.caption .divider{position:absolute;left:443px;top:8px;width:1px;height:50px;background:#555}
.thumb{top:9px;width:91px;height:48px;border:1px solid #444}
.thumb.on{border:2px solid #e0399a}

.welcome-dot{left:117px;top:595px;width:34px;height:34px;border-radius:50%;background:var(--white)}
.welcome{left:163px;top:594px;font-family:'Kaushan Script',cursive;font-size:27px;color:var(--blue);letter-spacing:3px;word-spacing:8px;white-space:nowrap}
.intro-title{left:109px;top:632px;font-family:'Ubuntu',sans-serif;font-weight:300;font-size:22px;letter-spacing:3.2px;white-space:nowrap}
.rule{left:109px;top:667px;width:860px;border-top:1px dotted #666}
.intro{left:109px;top:675px;width:870px;font-family:'Ubuntu',sans-serif;font-size:10.8px;line-height:18.5px;color:#eee}

.card{top:773px;width:270px;height:305px;background:var(--panel)}
.card-dot{left:10px;top:-8px;width:54px;height:54px;border-radius:50%;background:var(--white);border:3px solid #555}
.card h2{position:absolute;left:71px;top:11px;font-family:'Ubuntu',sans-serif;font-weight:300;font-size:22px;white-space:nowrap;color:#e8e8e8;letter-spacing:.2px}
.card h2 span{color:var(--blue-light)}
.card-photo{left:11px;top:57px;width:244px;height:109px;border:4px solid #5a5a5a}
.card p{position:absolute;left:6px;top:188px;width:250px;font-size:11.5px;line-height:18.5px;color:var(--grey-text);text-align:justify}
.more{left:182px;top:295px;width:77px;height:24px;border-radius:12px;background:linear-gradient(#3a9de2,#0b5da0);border:1px solid #7cc2f2;font-size:11.5px;text-align:center;line-height:22px;color:var(--white)}

.footer{left:0;top:1115px;width:1108px;height:85px;background:linear-gradient(#2a8fd6,#0c5ea3);border-top:1px solid #47a5e6}
.footer-logo{left:111px;top:8px;width:100px;text-align:center}
.footer-logo i{display:block;width:40px;height:40px;border-radius:50%;background:var(--white);margin:0 auto 6px}
.footer-logo span{font-family:'Ubuntu',sans-serif;font-size:13px;color:var(--white);white-space:nowrap}
.footer-links{left:385px;top:25px;font-size:11.5px;white-space:nowrap;word-spacing:1px}
.footer-links .sep{margin:0 20px}
.copy{left:417px;top:48px;font-size:11.5px;white-space:nowrap}
</style>
</head>
<body>

<header>
  <div class="abs topbar"></div>
  <div class="abs logo-tab">
    <span class="logo-dot"></span>
    <span class="logo-name">Brightway Merc</span>
  </div>
  <nav class="abs nav">
    <a class="active" href="#">our products</a>
    <a href="#" style="left:711px">our catalogues</a>
    <a href="#" style="left:863px">about us</a>
    <a href="#" style="left:979px">news</a>
  </nav>
  <div class="abs follow">Follow us on</div>
  <span class="abs social" style="left:872px" role="img" aria-label="Social network link"></span>
  <span class="abs social" style="left:905px" role="img" aria-label="Feed link"></span>
  <span class="abs social" style="left:938px" role="img" aria-label="Social network link"></span>
  <span class="abs social" style="left:971px" role="img" aria-label="Video channel link"></span>
  <div class="abs order"><b>ORDER ONLINE :</b> TEL: +1 800 555 0142</div>
</header>

<section class="abs slider">
  <div class="abs slide-photo" role="img" aria-label="Fashion photo: model in a net veil against a patterned beige wall">
    <span class="abs arrow prev"><svg style="left:50px" width="16" height="30"><path d="M14 1 L2 15 L14 29" fill="none" stroke="#333" stroke-width="1.5"/></svg></span>
    <span class="abs arrow next"><svg style="left:18px" width="16" height="30"><path d="M2 1 L14 15 L2 29" fill="none" stroke="#333" stroke-width="1.5"/></svg></span>
  </div>
  <div class="abs caption">
    <h3>The latest fashion shows.</h3>
    <p>Lorem ipsum dolor sit amet, consectetur adipiscing elit. Mauris non aliquam neque. Sed id ligula non purus scelerisque...</p>
    <span class="divider"></span>
    <span class="abs thumb" style="left:467px;background:linear-gradient(90deg,#ddd,#444)" role="img" aria-label="Thumbnail: model in black hat"></span>
    <span class="abs thumb" style="left:566px;background:linear-gradient(#cfd9de,#b8574c)" role="img" aria-label="Thumbnail: model by the sea"></span>
    <span class="abs thumb on" style="left:665px;background:linear-gradient(90deg,#cfd3d8,#f2f2f2)" role="img" aria-label="Thumbnail: man in white shirt"></span>
    <span class="abs thumb" style="left:764px;background:linear-gradient(90deg,#e8d9c2,#8a5a3a)" role="img" aria-label="Thumbnail: model with curly hair"></span>
  </div>
</section>

<section>
  <span class="abs welcome-dot"></span>
  <div class="abs welcome">Welcome to the</div>
  <h1 class="abs intro-title" style="font-weight:300">Brightway Merc Profilering Relame Gaver</h1>
  <div class="abs rule"></div>
  <p class="abs intro">Lorem ipsum dolor sit amet, consectetur adipiscing elit. Sed at ante. Mauris eleifend, quam a vulputate dictum, massa quam dapibus leo, eget vulputate orci purus ut lorem. In fringilla mi in ligula. Pellentesque aliquam quam vel dolor. Nunc adipiscing. Sed quam odio, tempus ac, aliquam molestie, varius ac, tellus. Vestibulum ut nulla aliquam risus rutrum interdum. Pellentesque lorem. Curabitur sit amet erat quis risus feugiat viverra. Pellentesque augue justo, sagittis et, lacinia at, venenatis non, arcu. Nunc nec libero. In cursus dictum risus...</p>
</section>

<article class="abs card" style="left:115px">
  <span class="abs card-dot"></span>
  <h2><span>Month Of</span> Product</h2>
  <div class="abs card-photo" style="background:linear-gradient(100deg,#2a2540,#8a86a8 45%,#4a4560)" role="img" aria-label="Product photo: model with windswept hair"></div>
  <p>simply dummy text of the printing and typesetting industry. Lorem Ipsum has been the industry's standard dummy text ever since the 1500s, when an unknown printer took a galley of type and scrambled it to make.</p>
  <span class="abs more">More Info</span>
</article>

<article class="abs card" style="left:421px">
  <span class="abs card-dot"></span>
  <h2><span>Brightway</span> News</h2>
  <div class="abs card-photo" style="background:linear-gradient(90deg,#3a3c40,#6b3048 55%,#c8c8c8)" role="img" aria-label="News photo: model in red dress on a balcony"></div>
  <p>simply dummy text of the printing and typesetting industry. Lorem Ipsum has been the industry's standard dummy text ever since the 1500s, when an unknown printer took a galley of type and scrambled it to make.</p>
  <span class="abs more">More Info</span>
</article>

<article class="abs card" style="left:728px">
  <span class="abs card-dot"></span>
  <h2><span>Brightway</span> Other</h2>
  <div class="abs card-photo" style="background:linear-gradient(90deg,#e6e6e6,#bdbdbd 50%,#ececec)" role="img" aria-label="Photo: man in white shirt with jacket over shoulder"></div>
  <p>simply dummy text of the printing and typesetting industry. Lorem Ipsum has been the industry's standard dummy text ever since the 1500s, when an unknown printer took a galley of type and scrambled it to make.</p>
  <span class="abs more">More Info</span>
</article>

<footer class="abs footer">
  <div class="abs footer-logo"><i></i><span>Brightway Merc</span></div>
  <div class="abs footer-links">Our products<span class="sep">|</span>Our catalogues<span class="sep">|</span>About us<span class="sep">|</span>News</div>
  <div class="abs copy">Copyright © Brightway Merc Northlane Web Studio</div>
</footer>

</body>
</html>
```